Bamboo & Ember Business Card FUN & EXCITING

Here is the Information for the Card:
Harpreet Kalra (Toby)
E: TobyKalra@mailbox-demo.com
C: (480) 555-0147
www.BambooEmberLV.com

We don't want traditional Indian cliche, We a playful bold and fun business card.

Files: https://files.sharebox-demo.net/folders/7QtpLmzR2xVbN4kHs9wYcDfJ3eGaUoPi

https://files.sharebox-demo.net/folders/5ZrqTwyX8mKcE2vBn6aLpHsQ9uFjRgOe

Target Market(s)

Las Vegas Local Restaurant

Industry/Entity Type

Indian Restaurant

Contact Information for Business Card

Name, Email, Cell Phone, Company Logo

```html
<!DOCTYPE html>
<html lang="en">
<head>
<meta charset="utf-8">
<title>Bamboo &amp; Ember – Business Card</title>
<link rel="stylesheet" href="https://fonts.googleapis.com/css2?family=Montserrat:wght@400;600;800&family=Oswald:wght@400&display=swap">
<style>
  :root {
    --backdrop: #2b2b2b;
    --card: #1d1d1d;
    --ink: #ffffff;
    --accent: #f08a2c;
    --muted: #cfcfcf;
    --art-a: #f2e6c8;
    --art-b: #ee8a3a;
  }
  * { box-sizing: border-box; margin: 0; padding: 0; }
  html, body { width: 1200px; height: 1108px; overflow: hidden; background: var(--backdrop); }
  body { position: relative; font-family: "Montserrat", sans-serif; color: var(--ink); }

  .card {
    position: absolute;
    left: 257px;
    width: 697px;
    background: var(--card);
    border-radius: 20px;
  }
  .card--front { top: 128px; height: 425px; }
  .card--back  { top: 594px; height: 440px; }

  .wordmark {
    position: absolute;
    font-weight: 800;
    color: var(--ink);
    text-transform: uppercase;
    line-height: 1;
    letter-spacing: -1px;
    white-space: nowrap;
  }
  .wordmark span { display: block; }
  .location {
    position: absolute;
    font-weight: 600;
    font-size: 14px;
    line-height: 1;
    color: var(--ink);
    text-align: right;
    white-space: nowrap;
  }
  .illustration {
    position: absolute;
    border-radius: 40px;
    background: radial-gradient(ellipse at 45% 45%, var(--art-a) 0%, #a8825a 45%, var(--art-b) 70%, rgba(29,29,29,0) 100%);
    opacity: 0.85;
  }
  .tagline {
    position: absolute;
    font-family: "Oswald", sans-serif;
    font-size: 11px;
    color: var(--muted);
    letter-spacing: 0.5px;
    text-align: center;
  }

  /* front */
  .card--front .wordmark { left: 243px; top: 104px; width: 226px; font-size: 44px; text-align: center; }
  .card--front .location { left: 243px; top: 206px; width: 226px; }
  .card--front .illustration { left: 243px; top: 245px; width: 226px; height: 118px; }
  .card--front .tagline { left: 243px; top: 367px; width: 226px; }

  /* back */
  .card--back .wordmark { left: 48px; top: 46px; width: 262px; font-size: 52px; }
  .card--back .location { left: 48px; top: 176px; width: 262px; }
  .contact { position: absolute; left: 49px; top: 226px; }
  .contact__name { font-weight: 600; font-size: 26px; color: var(--accent); line-height: 1.1; }
  .contact__role { font-size: 16px; color: var(--ink); margin-bottom: 20px; }
  .contact__list { list-style: none; }
  .contact__item { display: flex; align-items: center; gap: 12px; font-size: 16px; height: 26px; }
  .contact__item svg { width: 15px; height: 15px; fill: var(--accent); flex: none; }
  .contact__address { margin-top: 16px; font-size: 16px; line-height: 1.25; }
  .card--back .illustration { left: 420px; top: 236px; width: 245px; height: 168px; }
  .card--back .tagline { left: 420px; top: 410px; width: 245px; }
</style>
</head>
<body>

<section class="card card--front">
  <div class="wordmark"><span>Bamboo</span><span>&amp; Ember</span></div>
  <div class="location">Las Vegas, NV</div>
  <div class="illustration" role="img" aria-label="Cartoon curry bowl and naan bread walking together with hearts and sparkles"></div>
  <p class="tagline">“A match made in heaven”</p>
</section>

<section class="card card--back">
  <div class="wordmark"><span>Bamboo</span><span>&amp; Ember</span></div>
  <div class="location">Las Vegas, NV</div>

  <div class="contact">
    <p class="contact__name">Harpreet Kalra (Toby)</p>
    <p class="contact__role">owner</p>
    <ul class="contact__list">
      <li class="contact__item">
        <svg viewBox="0 0 16 16" aria-hidden="true"><path d="M2 6c0-2 2-3 6-3s6 1 6 3v1h-3V5.5H5V7H2zM4 8h8l2 5H2z"/></svg>
        (480) 555-0147
      </li>
      <li class="contact__item">
        <svg viewBox="0 0 16 16" aria-hidden="true"><path d="M1 4h14v9H1zM1 4l7 5 7-5v1.5L8 10.5 1 5.5z" fill-rule="evenodd"/></svg>
        TobyKalra@mailbox-demo.com
      </li>
      <li class="contact__item">
        <svg viewBox="0 0 16 16" aria-hidden="true"><circle cx="8" cy="8" r="7"/></svg>
        www.BambooEmberLV.com
      </li>
    </ul>
    <p class="contact__address">418 Juniper Ave, #112<br>Lakewood, OH 43099</p>
  </div>

  <div class="illustration" role="img" aria-label="Cartoon curry bowl and naan bread walking together with hearts and sparkles"></div>
  <p class="tagline">“A match made in heaven”</p>
</section>

</body>
</html>
```